Business Card Design

About Us
VaultNetix is a young and innovative company focusing on security and hosting solutions for global enterprise. To supply the high-performance, highly interconnected and low latency DDoS protection service, we distributed a large number of huge scrubbing centers all over the world. So VaultNetix is the first choice for enterprise to protect their network security.

Task detail
1. We hope that the business card can be filled with creativity, simple and technologe, the business card background is white, the business card text color and other colors are black, blue, green or your needs.

2. We need the source files provided by the successful bidder, such as *.psd, *.ai, etc.

3. One side contains the following:
-Logo
-Brin Sales Manager
-VAULTNETIX TECHNOLOGY CO., LIMITED
-Add:
9/F., Harmon Tower,
218 Pellow Street, Tai Hang, Kowloon,
HK
-Tel: 86-755-4172 0583
-Phone: 86-189 6041 3725
-Email: brin@vault-netix.com
-Web: www.vault-netix.com

4. The other side contains the following:
-Logo

5. Please find the attachment contains the logo PSD source files.

```html
<!DOCTYPE html>
<html lang="en">
<head>
<meta charset="utf-8">
<title>VaultNetix Business Card</title>
<link rel="stylesheet" href="https://fonts.googleapis.com/css2?family=Open+Sans:wght@400;600;700&display=swap">
<style>
  :root {
    --stage: #3a2f25;
    --card-black: #0d0f10;
    --cyan: #2fb9c9;
    --cyan-light: #58d3df;
    --cyan-dark: #1d94a3;
    --green: #9bdc4a;
    --white: #f2f4f4;
  }
  * { margin: 0; padding: 0; box-sizing: border-box; }
  html, body {
    width: 1200px; height: 1023px; overflow: hidden;
    background: var(--stage);
    font-family: "Open Sans", Arial, sans-serif;
  }
  .card {
    position: absolute; left: 250px; width: 700px; height: 400px;
    background: var(--card-black); overflow: hidden;
    box-shadow: 0 10px 30px rgba(0,0,0,.45);
  }
  .card--front { top: 90px; }
  .card--back { top: 533px; background: var(--cyan); }

  .brick-band {
    position: absolute; left: 0; width: 100%;
    background: linear-gradient(180deg, var(--cyan-light), var(--cyan) 50%, var(--cyan-dark));
  }
  .card--front .brick-band { height: 58px; }
  .brick-band--top { top: 0; }
  .brick-band--bottom { bottom: 0; }
  .brick-band--full { top: 0; height: 100%; }

  .company-name { font-weight: 600; color: var(--white); line-height: 1; white-space: nowrap; }

  .front-name { position: absolute; left: 60px; top: 170px; font-size: 46px; }

  .contact { position: absolute; left: 400px; top: 78px; width: 270px; color: var(--white); }
  .contact__name { color: var(--green); font-size: 24px; font-weight: 700; line-height: 1.1; }
  .contact__title { font-size: 14px; margin-bottom: 10px; }
  .contact__list { list-style: none; }
  .contact__item { display: flex; align-items: center; gap: 9px; font-size: 15px; line-height: 24px; }
  .contact__icon { width: 15px; height: 15px; flex: none; }
  .contact__rule { height: 1px; background: var(--cyan); margin: 12px 0 10px -40px; width: 300px; }
  .contact__address { color: var(--green); font-size: 15px; line-height: 23px; font-style: normal; }

  .back-band {
    position: absolute; left: 0; top: 120px; width: 100%; height: 160px;
    background: var(--card-black);
  }
  .back-notch { position: absolute; background: var(--card-black); }
  .back-notch--a { left: 70px; top: 98px; width: 60px; height: 24px; }
  .back-notch--b { left: 560px; top: 98px; width: 80px; height: 24px; }
  .back-notch--c { left: 40px; top: 278px; width: 90px; height: 24px; }
  .back-notch--d { left: 520px; top: 278px; width: 70px; height: 24px; }
  .back-name {
    position: absolute; left: 0; top: 167px; width: 100%;
    text-align: center; font-size: 66px;
  }
</style>
</head>
<body>

<section class="card card--front">
  <div class="brick-band brick-band--top" role="img" aria-label="Cyan brick wall pattern band"></div>
  <div class="brick-band brick-band--bottom" role="img" aria-label="Cyan brick wall pattern band"></div>

  <p class="company-name front-name">VaultNetix</p>

  <div class="contact">
    <p class="contact__name">Brin</p>
    <p class="contact__title">Sales Manager</p>
    <ul class="contact__list">
      <li class="contact__item">
        <svg class="contact__icon" viewBox="0 0 15 15"><rect width="15" height="15" rx="2" fill="#9bdc4a"/><path d="M4 3.5c0 4 3.5 7.5 7.5 7.5l.5-2-2-1-1 1c-1.2-.5-2.5-1.8-3-3l1-1-1-2z" fill="#0d0f10"/></svg>
        86-755-4172 0583
      </li>
      <li class="contact__item">
        <svg class="contact__icon" viewBox="0 0 15 15"><rect width="15" height="15" rx="2" fill="#9bdc4a"/><rect x="5" y="3" width="5" height="9" rx="1" fill="none" stroke="#0d0f10" stroke-width="1.3"/></svg>
        86-189 6041 3725
      </li>
      <li class="contact__item">
        <svg class="contact__icon" viewBox="0 0 15 15"><rect width="15" height="15" rx="2" fill="#9bdc4a"/><rect x="3" y="4.5" width="9" height="6" fill="none" stroke="#0d0f10" stroke-width="1.2"/><path d="M3 4.5l4.5 3.5 4.5-3.5" fill="none" stroke="#0d0f10" stroke-width="1.2"/></svg>
        brin@vault-netix.com
      </li>
      <li class="contact__item">
        <svg class="contact__icon" viewBox="0 0 15 15"><rect width="15" height="15" rx="2" fill="#9bdc4a"/><circle cx="7.5" cy="7.5" r="4" fill="none" stroke="#0d0f10" stroke-width="1.2"/><path d="M3.5 7.5h8M7.5 3.5v8" stroke="#0d0f10" stroke-width="1"/></svg>
        www.vault-netix.com
      </li>
    </ul>
    <div class="contact__rule"></div>
    <address class="contact__address">
      9/F., Harmon Tower<br>
      218 Pellow Street, Tai Hang<br>
      Kowloon, HK
    </address>
  </div>
</section>

<section class="card card--back">
  <div class="brick-band brick-band--full" role="img" aria-label="Cyan brick wall pattern background"></div>
  <div class="back-band"></div>
  <div class="back-notch back-notch--a"></div>
  <div class="back-notch back-notch--b"></div>
  <div class="back-notch back-notch--c"></div>
  <div class="back-notch back-notch--d"></div>
  <p class="company-name back-name">VaultNetix</p>
</section>

</body>
</html>
```